Stationary Design For New Dynamic Company

Hi there we require stationary designed for our new company, we have used "Sketch Meadow" recently for our logo and were very impressed with all of the designers that contributed towards the final result.
What we require now is the following:
Letter head layout (A4)
Business Cards (5 people)
With Compliments slips
Envelopes
Email stationary
We would like to use our current logo design and I have included it for your use (JPEG is the one we have chosen and I have attached an EPS file for your use). Our company specializes in architectural cladding and our products are used by architects, builders and private clients, so we wish for the stationary to be suitable and attractive to our clientele.
I thank everyone in advance for your contributions.
Thank you to all that have provided your designs for this project, I apologize for not providing feedback as I have been away. I have looked at everyone's designs and they all look great and I will come back to those designers that I wish to have changes made sometime today.
Once again a big thank you to all involved.

```html
<!DOCTYPE html>
<html lang="en">
<head>
<meta charset="utf-8">
<title>Stratawall Stationery</title>
<link rel="stylesheet" href="https://fonts.googleapis.com/css2?family=Source+Sans+3:wght@400;600;700&display=swap">
<style>
  :root {
    --navy: #0b3a63;
    --orange: #f7941d;
    --paper: #ffffff;
    --ink: #1d2b3a;
    --stage: #ffffff;
    --shadow: rgba(0, 0, 0, 0.45);
  }
  * { box-sizing: border-box; margin: 0; padding: 0; }
  html, body {
    width: 1200px; height: 900px; overflow: hidden;
    background: var(--stage);
    font-family: "Source Sans 3", Arial, sans-serif;
    color: var(--navy);
  }
  .sheet {
    position: absolute;
    background: var(--paper);
    box-shadow: 6px 6px 12px var(--shadow);
  }

  .brand {
    position: absolute;
    display: flex; align-items: center; gap: 0.3em;
    font-weight: 700; line-height: 1; letter-spacing: 0.01em;
    color: var(--navy); white-space: nowrap;
  }
  .brand-square {
    width: 0.8em; height: 0.8em; background: var(--orange); flex: none;
  }

  .contact {
    position: absolute;
    font-size: 11px; font-weight: 700; line-height: 14px;
    color: var(--navy); white-space: nowrap;
  }

  /* Letterhead */
  .letterhead { left: 20px; top: 37px; width: 594px; height: 841px; }
  .letterhead .brand { left: 72px; top: 770px; font-size: 32px; }
  .letterhead .contact-main { left: 95px; top: 802px; }
  .letterhead .contact-web { left: 279px; top: 802px; }

  /* Business card front */
  .card-front { left: 371px; top: 74px; width: 241px; height: 152px; }
  .card-front .brand { left: 14px; top: 26px; font-size: 19px; }
  .card-details {
    position: absolute; left: 0; top: 74px; width: 126px; height: 64px;
    background: var(--navy); color: #fff;
    font-size: 9.5px; line-height: 12px; padding: 3px 0 0 14px;
    white-space: nowrap;
  }
  .card-details .email { color: var(--orange); }
  .card-person {
    position: absolute; left: 126px; top: 74px; width: 115px; height: 64px;
    background: var(--orange); color: #fff; text-align: right;
    padding: 15px 12px 0 0;
  }
  .card-person .name { font-size: 13px; line-height: 15px; }
  .card-person .role { font-size: 10.5px; line-height: 13px; }

  /* Business card back */
  .card-back { left: 627px; top: 74px; width: 241px; height: 152px; }
  .card-back .brand { left: 52px; top: 66px; font-size: 19px; }

  /* Compliments slip */
  .comp-slip { left: 583px; top: 60px; width: 607px; height: 421px; }
  .comp-slip .slip-headline {
    position: absolute; left: 72px; top: 348px;
    display: flex; align-items: flex-end; gap: 18px; white-space: nowrap;
  }
  .comp-slip .slip-headline .brand { position: static; font-size: 32px; }
  .comp-slip .tagline {
    font-size: 29px; font-weight: 600; line-height: 1; color: var(--navy);
  }
  .comp-slip .contact-main { left: 95px; top: 383px; }
  .comp-slip .contact-web { left: 279px; top: 383px; }

  /* Envelope */
  .envelope { left: 555px; top: 538px; width: 623px; height: 312px; }
  .stamp {
    position: absolute; left: 563px; top: 40px; width: 42px; height: 32px;
    border: 2px dotted #8a8f96; background: var(--paper);
    display: flex; align-items: center; justify-content: center;
  }
  .stamp span { width: 18px; height: 18px; background: var(--navy); }
  .recipient {
    position: absolute; left: 283px; top: 111px;
    font-size: 11px; line-height: 14.5px; color: var(--ink);
  }
  .envelope .brand { left: 74px; top: 240px; font-size: 32px; }
  .envelope .contact-main { left: 95px; top: 272px; }
  .envelope .contact-web { left: 279px; top: 272px; }
</style>
</head>
<body>

  <section class="sheet letterhead" aria-label="Letterhead">
    <div class="brand"><span class="brand-square"></span>STRATAWALL</div>
    <p class="contact contact-main">0123 456 789<br>Address - City - PostCode</p>
    <p class="contact contact-web">info@stratawall.com<br>www.stratawall.com</p>
  </section>

  <section class="sheet comp-slip" aria-label="With compliments slip">
    <div class="slip-headline">
      <div class="brand"><span class="brand-square"></span>STRATAWALL</div>
      <p class="tagline">with complements</p>
    </div>
    <p class="contact contact-main">0123 456 789<br>Address - City - PostCode</p>
    <p class="contact contact-web">info@stratawall.com<br>www.stratawall.com</p>
  </section>

  <section class="sheet card-front" aria-label="Business card front">
    <div class="brand"><span class="brand-square"></span>STRATAWALL</div>
    <div class="card-details">
      0123 456 678<br>Your Address<br>Post Code<br>City<br>
      <span class="email">sam@stratawall.com</span>
    </div>
    <div class="card-person">
      <p class="name">Sam Porter</p>
      <p class="role">Director</p>
    </div>
  </section>

  <section class="sheet card-back" aria-label="Business card back">
    <div class="brand"><span class="brand-square"></span>STRATAWALL</div>
  </section>

  <section class="sheet envelope" aria-label="Envelope">
    <div class="stamp"><span></span></div>
    <p class="recipient">To Client<br>Address<br>Post Code<br>City</p>
    <div class="brand"><span class="brand-square"></span>STRATAWALL</div>
    <p class="contact contact-main">0123 456 789<br>Address - City - PostCode</p>
    <p class="contact contact-web">info@stratawall.com<br>www.stratawall.com</p>
  </section>

</body>
</html>
```